IT COMPANYcutting edge tec business card

we are IT company that building any apps.
we need business card in japanese and english
You don’t have to include all information in front one you can attach part of that information to back-side
company name : 株式会社ひかりの丘 (BRIGHTHILL Inc.)
concept : cutting-edge technology
role : 取締役 (director)
name : 呉 炫秀 (Oh Hyeonsuk)
post number : 154-0038
address : 東京都世田谷区西若葉台5-14-8 (5-14-8, Nishiwakabadai, Setagaya Ku, Tokyo To, 154-0038, Japan)
Tel:+81-3-5917-2846
Mobile:+81-80-7253-3169
Email : hoh@brighthill-lab.com
website : www.brighthill-lab.com

we dont have logo so please make it as well
we also looking for designer who can make homapage design.

Contact Information for Business Card

cutting-edge design and modern for IT

Font styles to use
Sans Serif

Colors
34a6d7
33b8a4
6092c4
3377b5
886aae
6b449b
b868aa
a64599

Requirements
Must have
• Simple but designed

```html
<!DOCTYPE html>
<html lang="en">
<head>
<meta charset="utf-8">
<title>BRIGHTHILL Inc. — Business Card</title>
<link rel="stylesheet" href="https://fonts.googleapis.com/css2?family=Roboto:ital,wght@0,400;0,500;0,700;1,700&family=Noto+Sans+JP:wght@400;500;700&display=swap">
<style>
  :root {
    --stage: #1c1c1d;
    --card-white: #f7f7f7;
    --card-black: #1a1a1b;
    --pattern-tone: #141415;
    --ink: #2a2a2a;
    --ink-soft: #4a4a4a;
    --accent-red: #cf2236;
    --faint: #e9e9e9;
  }
  * { box-sizing: border-box; margin: 0; padding: 0; }
  html, body {
    width: 1200px; height: 973px; overflow: hidden;
    background: var(--stage);
  }
  .stage {
    position: relative; width: 1200px; height: 973px;
  }
  .card {
    position: absolute; top: 336px;
    width: 520px; height: 300px;
    border-radius: 18px;
    overflow: hidden;
  }
  .card--front {
    left: 60px; background: var(--card-white);
    font-family: "Roboto", "Noto Sans JP", sans-serif;
    color: var(--ink);
  }
  .card--back { left: 620px; background: var(--card-black); }

  .holder { position: absolute; left: 34px; top: 32px; }
  .holder__name {
    font-weight: 700; font-style: italic; font-size: 15px;
    letter-spacing: 0.3px; color: var(--accent-red); text-transform: uppercase;
  }
  .holder__role {
    font-size: 9px; font-weight: 500; letter-spacing: 0.4px;
    margin-top: 2px; text-transform: uppercase; color: var(--ink-soft);
  }

  .contact {
    position: absolute; left: 34px; top: 102px;
    font-size: 11px; line-height: 16px; color: var(--ink-soft);
  }
  .contact__row { display: flex; }
  .contact__label { width: 38px; }
  .contact__web { margin-top: 8px; }
  .contact__web b { font-weight: 700; color: var(--ink); }
  .contact__address { margin-top: 8px; }

  .holder-jp {
    position: absolute; left: 372px; top: 104px;
    font-family: "Noto Sans JP", sans-serif;
  }
  .holder-jp__name {
    font-size: 18px; font-weight: 700; color: var(--accent-red); letter-spacing: 4px;
  }
  .holder-jp__role { font-size: 11px; color: var(--ink-soft); margin-top: 1px; }

  .faint-mark {
    position: absolute; right: 34px; top: 150px;
    width: 90px; height: 90px; border-radius: 50%;
    background: var(--faint);
  }

  .wordmark {
    position: absolute; right: 34px; top: 196px;
    font-family: "Roboto", sans-serif; font-weight: 400;
    font-size: 36px; letter-spacing: -0.5px; color: var(--ink);
  }
  .address-jp {
    position: absolute; right: 34px; top: 248px;
    font-family: "Noto Sans JP", sans-serif; font-size: 12px;
    color: var(--ink-soft); letter-spacing: 0.5px;
  }

  .back-pattern {
    position: absolute; inset: 0;
    background: linear-gradient(160deg, var(--card-black), var(--pattern-tone));
  }
  .back-mark {
    position: absolute; right: 80px; top: 150px;
    font-family: "Roboto", sans-serif; font-weight: 400;
    font-size: 14px; letter-spacing: 1px; color: var(--card-white);
  }
</style>
</head>
<body>
<main class="stage">
  <section class="card card--front" aria-label="Business card front">
    <div class="holder">
      <p class="holder__name">Oh Hyeonsuk</p>
      <p class="holder__role">Director</p>
    </div>

    <div class="contact">
      <p class="contact__row"><span class="contact__label">tel</span><span>+81-3-5917-2846</span></p>
      <p class="contact__row"><span class="contact__label">mob.</span><span>+81-80-7253-3169</span></p>
      <p class="contact__row"><span class="contact__label">email</span><span>hoh@brighthill-lab.com</span></p>
      <p class="contact__web">www.<b>brighthill-lab</b>.com</p>
      <p class="contact__address">5-14-8, Nishiwakabadai<br>Setagaya Ku, Tokyo To, 154-0038, Japan</p>
    </div>

    <div class="holder-jp">
      <p class="holder-jp__name">呉 炫秀</p>
      <p class="holder-jp__role">取締役</p>
    </div>

    <div class="faint-mark" aria-hidden="true"></div>
    <p class="wordmark">BRIGHTHILL</p>
    <p class="address-jp">東京都世田谷区西若葉台5-14-8</p>
  </section>

  <section class="card card--back" aria-label="Business card back">
    <div class="back-pattern" role="img" aria-label="Dark tone-on-tone repeating pattern covering the card back"></div>
    <p class="back-mark">BRIGHTHILL</p>
  </section>
</main>
</body>
</html>
```